Create a business promotion flyer to leave in customer mailboxes. We are a bulk petroleum supplier, servicing any industry that requires diesel. Base in griffith NSW, servicing griffith area and surrounds.

Business Name - Terra Petro
Fuel@terrapetro-example.com.au
Marco - 0400 000 001 mtorrisi@terrapetro-example.com.au
Liam - 0400 000 002 lharcourt@terrapetro-example.com.au
Peter - 0400 000 003 pwinslow@terrapetro-example.com.au
Office 02 5550 0100

Bulk Fuel deliveries.
Oils & lubricants
Local Family owned business

```html
<!DOCTYPE html>
<html lang="en">
<head>
<meta charset="utf-8">
<title>Terra Petro – Bulk Fuel Flyer</title>
<link href="https://fonts.googleapis.com/css2?family=Anton&family=Montserrat:ital,wght@0,400;0,500;0,600;0,700;0,800;1,800&display=swap" rel="stylesheet">
<style>
  :root {
    --red: #e3241b;
    --red-deep: #b8160f;
    --charcoal: #2b2d31;
    --ink: #2f3034;
    --white: #ffffff;
    --rule: #c9c9c9;
    --sky: #8fb6dc;
    --ground: #cfcac4;
  }
  * { margin: 0; padding: 0; box-sizing: border-box; }
  html, body { width: 731px; height: 1200px; overflow: hidden; background: var(--white); }
  .flyer {
    position: relative; width: 731px; height: 1200px; overflow: hidden;
    font-family: "Montserrat", Arial, sans-serif; color: var(--ink);
  }
  .backdrop { position: absolute; inset: 0; }
  .abs { position: absolute; }

  .brand-name {
    left: 34px; top: 112px; font-size: 41px; font-weight: 500;
    color: var(--red); letter-spacing: -0.5px; white-space: nowrap;
  }
  .header-rule { left: 309px; top: 24px; width: 2px; height: 222px; background: var(--red); }

  .headline {
    left: 337px; font-family: "Anton", Impact, sans-serif; font-size: 44px;
    line-height: 1; transform: scaleY(1.35); transform-origin: top left;
    white-space: nowrap; color: var(--ink);
  }
  .headline--one { top: 30px; }
  .headline--two { top: 92px; }
  .headline .accent { color: var(--red); }

  .service-area {
    left: 337px; top: 157px; width: 358px; height: 26px; background: var(--red);
    color: var(--white); font-weight: 700; font-size: 15.5px; line-height: 26px;
    text-align: center; white-space: nowrap;
  }
  .intro { left: 337px; top: 207px; width: 380px; font-size: 12.5px; font-weight: 500; line-height: 1.4; }

  .banner-title {
    left: 34px; top: 556px; font-family: "Anton", Impact, sans-serif; font-size: 35px;
    line-height: 1; color: var(--white); transform: scaleY(1.3); transform-origin: top left; white-space: nowrap;
  }
  .banner-sub { left: 34px; top: 613px; font-size: 18px; font-weight: 600; color: var(--white); white-space: nowrap; }

  .service { position: absolute; left: 0; width: 330px; height: 90px; }
  .service__icon { position: absolute; left: 36px; top: 4px; width: 66px; height: 66px; }
  .service__title {
    position: absolute; left: 115px; top: 0; font-size: 14.5px; font-weight: 800;
    line-height: 1; color: var(--white); text-transform: uppercase;
  }
  .service__mark { position: absolute; left: 115px; top: 33px; width: 60px; height: 3px; background: var(--red); }
  .service__text { position: absolute; left: 115px; top: 40px; font-size: 9.5px; font-weight: 500; line-height: 1.12; color: var(--white); }

  .divider { position: absolute; left: 32px; width: 284px; height: 1px; background: #6a6c70; }

  .location-label { left: 513px; top: 625px; font-size: 12px; font-weight: 600; color: var(--red); }
  .location-town { left: 513px; top: 640px; font-size: 19px; font-weight: 800; line-height: 0.95; color: var(--ink); }
  .location-note { left: 513px; top: 690px; font-size: 11.5px; font-weight: 500; line-height: 1; color: var(--red); }

  .contact { position: absolute; left: 513px; }
  .contact__name { font-size: 12.5px; font-weight: 600; color: var(--red); line-height: 1; text-transform: uppercase; }
  .contact__phone { font-size: 20px; font-weight: 700; color: var(--ink); line-height: 1.05; white-space: nowrap; }
  .contact__email { font-size: 9.6px; font-weight: 500; color: var(--red); line-height: 1.2; white-space: nowrap; }

  .rule { position: absolute; left: 513px; width: 176px; height: 1px; background: var(--rule); }

  .main-email {
    left: 477px; top: 1013px; font-family: "Anton", Impact, sans-serif; font-size: 16.5px;
    line-height: 1; transform: scaleY(1.35); transform-origin: top left; color: var(--ink); white-space: nowrap;
  }

  .tagline {
    left: 0; width: 731px; top: 1146px; text-align: center; font-size: 14.5px;
    font-weight: 800; font-style: italic; color: var(--white); letter-spacing: 0.2px;
  }
</style>
</head>
<body>
<main class="flyer">

  <svg class="backdrop" width="731" height="1200" viewBox="0 0 731 1200" aria-hidden="false">
    <defs>
      <linearGradient id="photoTone" x1="0" y1="0" x2="0" y2="1">
        <stop offset="0" stop-color="var(--sky)"/>
        <stop offset="0.45" stop-color="#dfe6ee"/>
        <stop offset="0.7" stop-color="#b9bcc0"/>
        <stop offset="1" stop-color="var(--ground)"/>
      </linearGradient>
      <linearGradient id="redWedge" x1="0" y1="0" x2="1" y2="1">
        <stop offset="0" stop-color="var(--red)"/>
        <stop offset="1" stop-color="var(--red-deep)"/>
      </linearGradient>
    </defs>

    <rect x="0" y="240" width="731" height="430" fill="url(#photoTone)" role="img"
          aria-label="Photo of two white fuel tanker road trains parked outside a depot shed"/>

    <polygon points="0,0 731,0 731,246 316,258 0,196" fill="var(--white)"/>
    <polygon points="0,196 316,258 0,372" fill="url(#redWedge)" opacity="0.92"/>

    <path d="M0,663 L400,663 C520,632 640,620 731,614 L731,1200 L0,1200 Z" fill="var(--white)"/>

    <path d="M0,589 L424,589 C412,760 388,950 342,1132 L0,1132 Z" fill="var(--charcoal)"/>
    <polygon points="0,550 398,550 352,647 0,647" fill="var(--red)"/>

    <path d="M0,1124 C240,1092 480,1072 731,1068 L731,1167 C480,1126 240,1116 0,1127 Z" fill="var(--red)"/>
    <path d="M0,1127 C240,1116 480,1126 731,1167 L731,1200 L0,1200 Z" fill="var(--charcoal)"/>

    <!-- location pin -->
    <g class="icon-pin" fill="none" stroke="var(--red)" stroke-width="3">
      <ellipse cx="450" cy="694" rx="18" ry="5"/>
      <path d="M450,690 C438,674 431,665 431,655 A19,19 0 0 1 469,655 C469,665 462,674 450,690 Z" fill="var(--red)" stroke="none"/>
      <circle cx="450" cy="655" r="6.5" fill="var(--white)" stroke="none"/>
    </g>

    <!-- phone & mail small icons -->
    <g fill="none" stroke="var(--red)" stroke-width="1.6">
      <circle cx="448" cy="756" r="10"/>
      <path d="M443.5,751 l2.5,-1.5 l2,3.5 l-1.6,1.2 c0.8,2 2,3.2 3.6,4 l1.2,-1.6 l3.5,2 l-1.5,2.5 c-5.5,-0.5 -9.5,-4.5 -9.7,-10.1 z" fill="var(--red)" stroke="none"/>
      <circle cx="448" cy="790" r="10"/>
      <rect x="441.5" y="785.5" width="13" height="9" rx="1"/>
      <path d="M441.5,786 L448,791 L454.5,786"/>
    </g>

    <!-- main email icon -->
    <g fill="none" stroke="var(--red)" stroke-width="2.2">
      <circle cx="447" cy="1027" r="21"/>
      <rect x="435" y="1018" width="24" height="17" rx="1.5" fill="var(--red)" stroke="none"/>
      <path d="M435.5,1019 L447,1028 L458.5,1019" stroke="var(--white)" stroke-width="1.8"/>
    </g>
  </svg>

  <div class="abs brand-name">Terra Petro</div>
  <div class="abs header-rule"></div>

  <div class="abs headline headline--one">YOUR LOCAL</div>
  <div class="abs headline headline--two"><span class="accent">BULK FUEL</span> SUPPLIER</div>
  <div class="abs service-area">SERVICING GRIFFITH &amp; SURROUNDS</div>
  <p class="abs intro">We supply high quality fuel and lubricants to keep your business and machinery running smoothly.</p>

  <div class="abs banner-title">BULK FUEL DELIVERIES</div>
  <div class="abs banner-sub">Reliable. Local. Family Owned</div>

  <section class="services">
    <div class="service" style="top:669px">
      <svg class="service__icon" viewBox="0 0 66 66" aria-hidden="true">
        <circle cx="33" cy="33" r="30" fill="none" stroke="#fff" stroke-width="2.5"/>
        <g fill="#fff">
          <rect x="13" y="24" width="26" height="14" rx="7"/>
          <path d="M41,27 h7 l5,7 v6 h-12 z"/>
          <rect x="12" y="39" width="41" height="3"/>
          <circle cx="19" cy="44" r="3.5"/><circle cx="33" cy="44" r="3.5"/><circle cx="47" cy="44" r="3.5"/>
        </g>
      </svg>
      <div class="service__title">Bulk Fuel<br>Deliveries</div>
      <div class="service__mark"></div>
      <p class="service__text">Reliable, on-time fuel<br>delivered to your farm,<br>site or business.</p>
    </div>
    <div class="divider" style="top:758px"></div>

    <div class="service" style="top:766px">
      <svg class="service__icon" viewBox="0 0 66 66" aria-hidden="true">
        <circle cx="33" cy="33" r="30" fill="none" stroke="#fff" stroke-width="2.5"/>
        <path d="M30,17 C25,26 20,31 20,38 A10,10 0 0 0 40,38 C40,31 35,26 30,17 Z" fill="#fff"/>
        <path d="M42,22 C40,26 38,28 38,31 A4,4 0 0 0 46,31 C46,28 44,26 42,22 Z" fill="#fff"/>
      </svg>
      <div class="service__title">Oils &amp;<br>Lubricants</div>
      <div class="service__mark"></div>
      <p class="service__text">Reliable, on-time fuel<br>delivered to your farm,<br>site or business.</p>
    </div>
    <div class="divider" style="top:860px"></div>

    <div class="service" style="top:868px">
      <svg class="service__icon" viewBox="0 0 66 66" aria-hidden="true">
        <circle cx="33" cy="33" r="30" fill="none" stroke="#fff" stroke-width="2.5"/>
        <g fill="#fff">
          <path d="M24,26 l10,-6 l8,4 l-3,5 l-6,1 l-5,10 l-6,-3 z"/>
          <rect x="40" y="20" width="9" height="4" rx="1" transform="rotate(25 44 22)"/>
          <path d="M20,40 l5,2 l-4,8 l-4,-2 z"/>
          <path d="M44,36 C42,40 41,41 41,43 A3,3 0 0 0 47,43 C47,41 46,40 44,36 Z"/>
        </g>
      </svg>
      <div class="service__title">Petrol<br>Deliveries</div>
      <div class="service__mark"></div>
      <p class="service__text">Reliable, on-time fuel<br>delivered to your farm,<br>site or business.</p>
    </div>
    <div class="divider" style="top:962px"></div>

    <div class="service" style="top:970px">
      <svg class="service__icon" viewBox="0 0 66 66" aria-hidden="true">
        <circle cx="33" cy="33" r="30" fill="none" stroke="#fff" stroke-width="2.5"/>
        <g fill="#fff">
          <circle cx="24" cy="22" r="5"/><path d="M16,44 v-11 a8,8 0 0 1 16,0 v11 z"/>
          <circle cx="42" cy="22" r="5"/><path d="M34,44 v-11 a8,8 0 0 1 16,0 v11 z"/>
          <circle cx="33" cy="32" r="4"/><path d="M27,48 v-7 a6,6 0 0 1 12,0 v7 z"/>
        </g>
      </svg>
      <div class="service__title">Local Family<br>Owned Business</div>
      <div class="service__mark"></div>
      <p class="service__text">Reliable, on-time fuel<br>delivered to your farm,<br>site or business.</p>
    </div>
  </section>

  <div class="abs location-label">BASED IN</div>
  <div class="abs location-town">GRIFFITH<br>NSW</div>
  <div class="abs location-note">Servicing griffith area<br>and surrounds</div>
  <div class="rule" style="top:723px"></div>

  <div class="contact" style="top:744px">
    <div class="contact__name">Marco</div>
    <div class="contact__phone">0400 000 001</div>
    <div class="contact__email">mtorrisi@terrapetro-example.com.au</div>
  </div>
  <div class="rule" style="top:806px"></div>

  <div class="contact" style="top:818px">
    <div class="contact__name">Liam</div>
    <div class="contact__phone">0400 000 002</div>
    <div class="contact__email">lharcourt@terrapetro-example.com.au</div>
  </div>
  <div class="rule" style="top:876px"></div>

  <div class="contact" style="top:886px">
    <div class="contact__name">Peter</div>
    <div class="contact__phone">0400 000 003</div>
    <div class="contact__email">pwinslow@terrapetro-example.com.au</div>
  </div>
  <div class="rule" style="top:944px"></div>

  <div class="contact" style="top:955px">
    <div class="contact__name">Office</div>
    <div class="contact__phone">02 5550 0100</div>
  </div>

  <div class="abs main-email">FUEL@TERRAPETRO-EXAMPLE.COM.AU</div>

  <div class="abs tagline">FUELING YOUR BUSINESS. POWERING OUR COMMUNITY.</div>
</main>
</body>
</html>
```